Interior Styling Workshop needs a brochure designed.

Hue Harbor is an interior design firm based in Sydney. We will be running Interior Styling Workshops
for all people interested in learning how to decorate
their home. It is important to show modern interior images to attract and excite their creative juices!
Colours we would like is a dark charcoal background
with Chartreuse trim for our logo and for the brochure.
We have attached some of our ideas on wording.
Our images can be replaced or changed to suit your
design.
The final design should be very stylish and to instill a desire to attend our workshops!

Target Market(s)

Mainly female adults in Sydney, aged approx. 25 to 60, who are interested in
interior decorating their homes.

Industry/Entity Type

Learning

Colors
5c5c5c
acd036

Requirements
Must have
• Must show good visual images to catch attention.
Nice to have
• Page layout i.e. to uploaded document, but open to any designs that work better.

```html
<!DOCTYPE html>
<html lang="en">
<head>
<meta charset="utf-8">
<title>Interior Styling Workshop – Brochure</title>
<link rel="stylesheet" href="https://fonts.googleapis.com/css2?family=Archivo+Black&family=Questrial&family=Arimo:wght@400;700&display=swap">
<style>
:root{
  --charcoal:#4a4f53;
  --charcoal-deep:#3f4447;
  --chartreuse:#acd036;
  --white:#ffffff;
  --stage:#111214;
  --frame:#d9dcdd;
}
*{box-sizing:border-box;margin:0;padding:0}
html,body{width:1200px;height:900px;overflow:hidden;background:var(--stage)}
.canvas{position:relative;width:1200px;height:900px}
.spread{position:absolute;top:218px;width:592px;height:460px;background:var(--charcoal);overflow:hidden;font-family:"Questrial",sans-serif;color:var(--white)}
.spread--outside{left:4px}
.spread--inside{left:604px}
.abs{position:absolute}
.photo{position:absolute}
/* outside */
.outside-top{position:absolute;inset:0;width:592px;height:460px}
.learn-title{left:18px;top:130px;font-size:15px;font-weight:700;color:var(--chartreuse);font-family:"Arimo",sans-serif}
.learn-list{left:18px;top:158px;width:180px;list-style:none;font-size:10.5px;line-height:1.25}
.learn-list li{position:relative;padding-left:14px;margin-bottom:10px}
.learn-list li svg{position:absolute;left:0;top:1px}
.learn-note{left:18px;top:392px;width:184px;font-size:10.5px;line-height:1.25}
.info-box{left:203px;top:155px;width:188px;height:286px;border:1px solid var(--frame);padding:16px 10px 0 11px}
.info-box__facts{font-family:"Arimo",sans-serif;font-weight:700;color:var(--chartreuse);font-size:11px;line-height:1.3}
.info-box__facts p{margin-bottom:12px}
.info-box__contact{margin-top:30px;text-align:center;font-size:11.5px;line-height:1.3}
.info-box__contact .hl{color:var(--chartreuse)}
.cover{left:421px;top:36px;width:150px;height:300px;background:var(--white);border:1px solid #c9c9c9}
.cover__title{font-family:"Archivo Black",sans-serif;color:var(--chartreuse);-webkit-text-stroke:0.6px #6d7a2a;font-size:18.5px;line-height:1.32;text-align:center;margin-top:10px;letter-spacing:.3px}
.cover__photo{left:3px;top:107px;width:142px;height:190px;background:linear-gradient(100deg,#7b7468 0%,#b9b3a8 30%,#e7e5df 55%,#cfc3ad 80%,#a58a62 100%)}
.cover__tagline{left:421px;top:348px;width:150px;text-align:center;font-size:17px;line-height:1.25;letter-spacing:.3px}
.brand{left:421px;top:398px;width:150px;text-align:center;font-size:14px;color:var(--chartreuse);line-height:1}
/* inside */
.question-box{left:10px;top:15px;width:184px;height:284px;border:1px solid var(--frame);text-align:center;padding:14px 6px 0;font-size:12.5px;line-height:1.55}
.question-box p{margin-bottom:8px}
.question-box .hl{color:var(--chartreuse)}
.inside-photo-left{left:8px;top:312px;width:186px;height:148px;background:linear-gradient(160deg,#e6e4de 0%,#cfc9bf 40%,#6f8d8e 70%,#3d3a36 100%)}
.story{left:214px;top:252px;width:172px;font-family:"Arimo",sans-serif;font-size:8.6px;line-height:1.72;text-align:left}
.story .hl{color:var(--chartreuse)}
.framed{position:absolute;left:414px;width:172px;height:128px;background:var(--white);padding:6px}
.framed .photo{position:absolute;inset:6px}
</style>
</head>
<body>
<main class="canvas">

  <section class="spread spread--outside" aria-label="Brochure outside">
    <svg class="outside-top" viewBox="0 0 592 460" aria-hidden="true">
      <defs>
        <linearGradient id="room-one" x1="0" y1="0" x2="1" y2="1">
          <stop offset="0" stop-color="#dfe4e2"/><stop offset=".5" stop-color="#b9c2c0"/><stop offset="1" stop-color="#5a5f64"/>
        </linearGradient>
        <linearGradient id="room-two" x1="0" y1="0" x2="1" y2="1">
          <stop offset="0" stop-color="#5b4458"/><stop offset=".5" stop-color="#d7d4cf"/><stop offset="1" stop-color="#6b3450"/>
        </linearGradient>
      </defs>
      <rect x="0" y="0" width="592" height="140" fill="var(--white)"/>
      <rect x="0" y="0" width="198" height="135" fill="url(#room-one)"/>
      <rect x="203" y="0" width="188" height="135" fill="url(#room-two)"/>
      <path d="M0 126 C120 142 300 138 592 22 L592 460 L0 460 Z" fill="var(--charcoal)" stroke="var(--white)" stroke-width="4"/>
    </svg>
    <div class="photo" role="img" aria-label="Bright modern living room with white sofa and yellow armchair" style="left:0;top:0;width:198px;height:1px"></div>
    <div class="photo" role="img" aria-label="Lounge with grey sofa, purple feature wall and timber floor" style="left:203px;top:0;width:188px;height:1px"></div>

    <h2 class="abs learn-title">You will learn</h2>
    <ul class="abs learn-list">
      <li><svg width="10" height="10" viewBox="0 0 10 10"><path d="M1 5.5 L4 8.5 L9 1" fill="none" stroke="var(--chartreuse)" stroke-width="2"/></svg>Where and how to use colour, shape, form, and different textures to create a balanced and harmonious environment.</li>
      <li><svg width="10" height="10" viewBox="0 0 10 10"><path d="M1 5.5 L4 8.5 L9 1" fill="none" stroke="var(--chartreuse)" stroke-width="2"/></svg>Current styles and what inspires you.</li>
      <li><svg width="10" height="10" viewBox="0 0 10 10"><path d="M1 5.5 L4 8.5 L9 1" fill="none" stroke="var(--chartreuse)" stroke-width="2"/></svg>Space planning and furniture placement for your room to give a balanced and spacious feel.</li>
      <li><svg width="10" height="10" viewBox="0 0 10 10"><path d="M1 5.5 L4 8.5 L9 1" fill="none" stroke="var(--chartreuse)" stroke-width="2"/></svg>Where to start!</li>
      <li><svg width="10" height="10" viewBox="0 0 10 10"><path d="M1 5.5 L4 8.5 L9 1" fill="none" stroke="var(--chartreuse)" stroke-width="2"/></svg>How to bring it all together with the finishing touches.</li>
      <li><svg width="10" height="10" viewBox="0 0 10 10"><path d="M1 5.5 L4 8.5 L9 1" fill="none" stroke="var(--chartreuse)" stroke-width="2"/></svg>Why Concept plans and mood boards are important.</li>
    </ul>
    <p class="abs learn-note">You will also enjoy making your very own mood board which will give you insight and inspire you to commence your project with confidence.</p>

    <div class="abs info-box">
      <div class="info-box__facts">
        <p>All Materials and Lunch are provided.</p>
        <p>Bookings are essential.</p>
        <p>Numbers are limited to 10 per workshop</p>
        <p>Cost:&nbsp; $240 (including lunch)</p>
      </div>
      <p class="info-box__contact">For more information, dates, times and venues of upcoming workshops, please call Tess on Mob 0400123456, or visit our Website www.<span class="hl">hueharbor</span>.com.au</p>
    </div>

    <div class="abs cover">
      <h1 class="cover__title">INTERIOR<br>STYLING<br>WORKSHOP</h1>
      <div class="abs cover__photo" role="img" aria-label="Hallway with round mirror, timber console and white orchid"></div>
    </div>
    <p class="abs cover__tagline">FIND YOUR STYLE<br>BE INSPIRED</p>
    <p class="abs brand">Hue Harbor</p>
  </section>

  <section class="spread spread--inside" aria-label="Brochure inside">
    <div class="abs question-box">
      <p>Would you like to transform your home?</p>
      <p class="hl">Do you feel OVERWHELMED and CONFUSED as to Where to start?</p>
      <p>Are you unsure of a colour scheme, what type of furniture, Soft furnishings, accessories suit your home and lifestyle?</p>
      <p class="hl">Where to buy?</p>
      <p>What will suit your budget?</p>
    </div>
    <div class="photo inside-photo-left" role="img" aria-label="Bedroom with teal bedding beside a sunny window"></div>

    <p class="abs story"><span class="hl">Tess Marlow</span> and <span class="hl">Nina Calder</span> of HUE <span class="hl">HARBOR</span> Interior Design understand the frustration and confusion that D.I.Y. home decorators face and will be holding INTERIOR STYLING WORKSHOPS in which you will learn how to create innovative colour schemes and styles from concept to completion in a fun, hands on experience, surrounded by beautiful furniture, fabrics, soft furnishings and homewares that will get your creative juices flowing!</p>

    <div class="framed" style="top:28px"><div class="photo" role="img" aria-label="Warm lit bedroom with stone feature wall" style="background:linear-gradient(135deg,#3a2c22,#a98a5e 45%,#6e5a48 75%,#2a221c)"></div></div>
    <div class="framed" style="top:163px"><div class="photo" role="img" aria-label="Open dining area with timber floor and view" style="background:linear-gradient(160deg,#eae8e2,#c9c5bb 50%,#8a5a32 85%,#5e3b20)"></div></div>
    <div class="framed" style="top:298px"><div class="photo" role="img" aria-label="Living room with patterned armchairs and timber floor" style="background:linear-gradient(160deg,#ecebe6,#d3cfc6 45%,#9a6a3e 80%,#3c3a38)"></div></div>
  </section>

</main>
</body>
</html>
```